Plakat-Design für Softwareentwicklung
Zielgruppe
Gemeinsam mit den Kunden entwickelt Velmoria hochkomplexe, sicherheitskritische Komponenten im Bereich der Softwareentwicklung für Automotive, Medical, Avionik-, und Defence, sowie Industriesysteme, nach branchenüblichen Vorgehensmodellen und Vorgaben (https://www.velmoria-beispiel.de/).
Wir suchen ein Design für unsere Kalenderplakate für das Jahr 2019.
Die Kalenderplakate benötigen wir für unsere internen Mitarbeiter und Geschäftskunden/-partner (B2B).
Aufgabenstellung
In den letzten Jahren haben wir das Kalenderplakat sowohl in DIN A3 und DIN B1 anfertigen lassen.
Das Kalenderplakat sollte praktisch und optisch ansprechend gestaltet sein, sodass man es sich gerne als Jahresplaner in sein Büro hängt. Welche Bilder/Fotos Sie nutzen, welches Design Sie wählen, bleibt komplett Ihnen überlassen. Wir möchten hier Ihre Kreativität nicht einschränken.
Neben dem Kalender (Tage nach Monaten sortiert, die letzten beiden Monate von 2018 und die ersten beiden von 2020 bitte ebenfalls integrieren, Wochenende und Feiertage farblich hervorheben), sollten auch unsere Kontaktdaten und unser Logo auf dem Plakat abgebildet werden.
Unser Slogan lautet 'Enter perfect Engineering'.
Wir freuen uns auf Ihre Vorschläge!

```html
<!DOCTYPE html>
<html lang="de">
<head>
<meta charset="utf-8">
<title>Velmoria Kalender 2019</title>
<link href="https://fonts.googleapis.com/css2?family=Oswald:wght@300;400;500&display=swap" rel="stylesheet">
<style>
:root{
  --bg:#dcdcdc;
  --paper:#ffffff;
  --ink:#1e1e22;
  --ink-soft:#4a4a4f;
  --dark:#47474c;
  --green:#3f9477;
  --green-soft:#8bbfa8;
  --sage:#a7c6bb;
  --red:#e52521;
  --salmon:#ef8a6c;
  --muted:#77777c;
}
*{box-sizing:border-box;margin:0;padding:0}
html,body{width:871px;height:1200px;overflow:hidden;background:var(--bg);font-family:'Oswald',sans-serif}
.poster{position:absolute;left:39px;top:40px;width:796px;height:1124px;background:var(--paper)}
.visual{position:absolute;left:0;top:0;width:313px;height:1124px;
  background:linear-gradient(160deg,#6f6a55 0%,#2c3135 14%,#c9c69a 28%,#e9e6bd 36%,#6f8f93 48%,#2d3d45 58%,#8ea5a2 68%,#c8c6a0 80%,#d7d3a9 92%,#9c9a82 100%)}
.brand-band{position:absolute;left:0;top:18px;width:313px;height:111px;background:var(--dark)}
.brand-lockup{position:absolute;left:34px;top:30px;display:flex;align-items:center;gap:10px}
.brand-name{font-weight:300;font-size:35px;line-height:1;color:var(--sage);letter-spacing:.3px}
.brand-mark{width:20px;height:20px;border-radius:50%;background:var(--sage);margin-top:4px}
.slogan{position:absolute;left:40px;top:74px;font-weight:300;font-size:12px;line-height:1;color:#8b8b90}
.title-box{position:absolute;left:313px;top:18px;width:329px;height:111px;background:var(--dark);box-shadow:6px 5px 0 var(--sage)}
.title-year{position:absolute;left:0;right:0;top:22px;text-align:center;font-weight:500;font-size:38px;line-height:1;color:var(--green)}
.title-word{position:absolute;left:0;right:0;top:60px;text-align:center;font-weight:500;font-size:37px;line-height:1;color:#fff;letter-spacing:4px}
.contact{position:absolute;left:0;top:980px;width:313px;height:144px;background:var(--dark);color:#fff;font-size:12px;font-weight:300;line-height:13px}
.contact-row{position:absolute;left:58px;white-space:nowrap}
.contact-row strong{font-weight:500}
.contact-row .sep{color:var(--green)}
.icon{position:absolute;left:28px;width:16px;height:16px}
.month{position:absolute;width:133px}
.month h2{text-align:center;font-weight:400;font-size:13px;line-height:14px;color:var(--green);margin-bottom:3px}
.weekdays,.days{display:grid;grid-template-columns:repeat(7,19px);list-style:none;text-align:center}
.weekdays li{font-size:7.5px;font-weight:300;color:var(--ink-soft);line-height:10px;margin-bottom:3px}
.days li{font-size:9.5px;font-weight:500;color:var(--ink);line-height:20.7px}
.days li.off{color:var(--red)}
.six .days li{line-height:17.4px}
.prev h2,.next h2{color:var(--green-soft)}
.prev .days li,.next .days li{color:var(--muted);font-weight:400}
.prev .days li.off,.next .days li.off{color:var(--salmon)}
.s2{grid-column-start:2}.s3{grid-column-start:3}.s4{grid-column-start:4}.s5{grid-column-start:5}.s6{grid-column-start:6}.s7{grid-column-start:7}
</style>
</head>
<body>
<div class="poster">
  <div class="visual" role="img" aria-label="Foto: unscharfe Lichtspuren auf nächtlicher Straße in Grün-, Gelb- und Grautönen"></div>
  <div class="brand-band">
    <div class="brand-lockup">
      <div class="brand-name">Velmoria</div>
      <div class="brand-mark"></div>
    </div>
    <div class="slogan">Präzision in jeder Zeile.</div>
  </div>
  <div class="title-box">
    <div class="title-year">2019</div>
    <div class="title-word">KALENDER</div>
  </div>

  <div class="contact">
    <svg class="icon" style="top:23px" viewBox="0 0 16 16"><path d="M8 1a5 5 0 0 0-5 5c0 4 5 9 5 9s5-5 5-9a5 5 0 0 0-5-5z" fill="#fff"/><circle cx="8" cy="6" r="2" fill="#47474c"/></svg>
    <div class="contact-row" style="top:24px"><strong>HEADQUARTER</strong> <span class="sep">//</span> Lindenhofweg 14, 80469 Munich<br><span style="padding-left:78px">Germany</span></div>
    <svg class="icon" style="top:58px" viewBox="0 0 16 16"><path d="M4 1.5l2.5 3-1.5 2c.8 1.8 2.2 3.2 4 4l2-1.5 3 2.5-1.5 2.5C7 14 2 9 1.5 3z" fill="#fff"/></svg>
    <div class="contact-row" style="top:58px"><strong>PHONE</strong> <span class="sep">//</span> +49 89 500120 – 0<br><strong>FAX</strong> <span class="sep">//</span> +49 89 500120-99</div>
    <svg class="icon" style="top:96px" viewBox="0 0 16 16"><rect x="1" y="3" width="14" height="10" fill="none" stroke="#fff" stroke-width="1.2"/><path d="M1 3l7 6 7-6M1 13l5-5M15 13l-5-5" fill="none" stroke="#fff" stroke-width="1.2"/></svg>
    <div class="contact-row" style="top:97px;left:61px">info@velmoria-beispiel.de</div>
    <svg class="icon" style="top:120px" viewBox="0 0 16 16" fill="none" stroke="#fff" stroke-width="1"><circle cx="8" cy="8" r="6.5"/><ellipse cx="8" cy="8" rx="3" ry="6.5"/><path d="M1.5 8h13M2.5 4.5h11M2.5 11.5h11"/></svg>
    <div class="contact-row" style="top:121px;left:61px">www.velmoria-beispiel.de</div>
  </div>

  <!-- Vorjahr -->
  <section class="month prev" style="left:479px;top:152px">
    <h2>NOVEMBER</h2>
    <ol class="weekdays"><li>MO</li><li>DI</li><li>MI</li><li>DO</li><li>FR</li><li>SA</li><li>SO</li></ol>
    <ol class="days"><li class="s4">1</li><li>2</li><li class="off">3</li><li class="off">4</li><li>5</li><li>6</li><li>7</li><li>8</li><li>9</li><li class="off">10</li><li class="off">11</li><li>12</li><li>13</li><li>14</li><li>15</li><li>16</li><li class="off">17</li><li class="off">18</li><li>19</li><li>20</li><li>21</li><li>22</li><li>23</li><li class="off">24</li><li class="off">25</li><li>26</li><li>27</li><li>28</li><li>29</li><li>30</li></ol>
  </section>
  <section class="month prev six" style="left:627px;top:152px">
    <h2>DEZEMBER</h2>
    <ol class="weekdays"><li>MO</li><li>DI</li><li>MI</li><li>DO</li><li>FR</li><li>SA</li><li>SO</li></ol>
    <ol class="days"><li class="s6 off">1</li><li class="off">2</li><li>3</li><li>4</li><li>5</li><li>6</li><li>7</li><li class="off">8</li><li class="off">9</li><li>10</li><li>11</li><li>12</li><li>13</li><li>14</li><li class="off">15</li><li class="off">16</li><li>17</li><li>18</li><li>19</li><li>20</li><li>21</li><li class="off">22</li><li class="off">23</li><li>24</li><li class="off">25</li><li class="off">26</li><li>27</li><li>28</li><li class="off">29</li><li class="off">30</li><li>31</li></ol>
  </section>

  <!-- 2019 -->
  <section class="month" style="left:330px;top:310px">
    <h2>JANUAR</h2>
    <ol class="weekdays"><li>MO</li><li>DI</li><li>MI</li><li>DO</li><li>FR</li><li>SA</li><li>SO</li></ol>
    <ol class="days"><li class="s2 off">1</li><li>2</li><li>3</li><li>4</li><li class="off">5</li><li class="off">6</li><li>7</li><li>8</li><li>9</li><li>10</li><li>11</li><li class="off">12</li><li class="off">13</li><li>14</li><li>15</li><li>16</li><li>17</li><li>18</li><li class="off">19</li><li class="off">20</li><li>21</li><li>22</li><li>23</li><li>24</li><li>25</li><li class="off">26</li><li class="off">27</li><li>28</li><li>29</li><li>30</li><li>31</li></ol>
  </section>
  <section class="month" style="left:479px;top:310px">
    <h2>FEBRUAR</h2>
    <ol class="weekdays"><li>MO</li><li>DI</li><li>MI</li><li>DO</li><li>FR</li><li>SA</li><li>SO</li></ol>
    <ol class="days"><li class="s5">1</li><li class="off">2</li><li class="off">3</li><li>4</li><li>5</li><li>6</li><li>7</li><li>8</li><li class="off">9</li><li class="off">10</li><li>11</li><li>12</li><li>13</li><li>14</li><li>15</li><li class="off">16</li><li class="off">17</li><li>18</li><li>19</li><li>20</li><li>21</li><li>22</li><li class="off">23</li><li class="off">24</li><li>25</li><li>26</li><li>27</li><li>28</li></ol>
  </section>
  <section class="month" style="left:627px;top:310px">
    <h2>MÄRZ</h2>
    <ol class="weekdays"><li>MO</li><li>DI</li><li>MI</li><li>DO</li><li>FR</li><li>SA</li><li>SO</li></ol>
    <ol class="days"><li class="s5">1</li><li class="off">2</li><li class="off">3</li><li>4</li><li>5</li><li>6</li><li>7</li><li>8</li><li class="off">9</li><li class="off">10</li><li>11</li><li>12</li><li>13</li><li>14</li><li>15</li><li class="off">16</li><li class="off">17</li><li>18</li><li>19</li><li>20</li><li>21</li><li>22</li><li class="off">23</li><li class="off">24</li><li>25</li><li>26</li><li>27</li><li>28</li><li>29</li><li class="off">30</li><li class="off">31</li></ol>
  </section>

  <section class="month" style="left:330px;top:467px">
    <h2>APRIL</h2>
    <ol class="weekdays"><li>MO</li><li>DI</li><li>MI</li><li>DO</li><li>FR</li><li>SA</li><li>SO</li></ol>
    <ol class="days"><li>1</li><li>2</li><li>3</li><li>4</li><li>5</li><li class="off">6</li><li class="off">7</li><li>8</li><li>9</li><li>10</li><li>11</li><li>12</li><li class="off">13</li><li class="off">14</li><li>15</li><li>16</li><li>17</li><li>18</li><li class="off">19</li><li class="off">20</li><li class="off">21</li><li class="off">22</li><li>23</li><li>24</li><li>25</li><li>26</li><li class="off">27</li><li class="off">28</li><li>29</li><li>30</li></ol>
  </section>
  <section class="month" style="left:479px;top:469px">
    <h2>MAI</h2>
    <ol class="weekdays"><li>MO</li><li>DI</li><li>MI</li><li>DO</li><li>FR</li><li>SA</li><li>SO</li></ol>
    <ol class="days"><li class="s3 off">1</li><li>2</li><li>3</li><li class="off">4</li><li class="off">5</li><li>6</li><li>7</li><li>8</li><li>9</li><li>10</li><li class="off">11</li><li class="off">12</li><li>13</li><li>14</li><li>15</li><li>16</li><li>17</li><li class="off">18</li><li class="off">19</li><li>20</li><li>21</li><li>22</li><li>23</li><li>24</li><li class="off">25</li><li class="off">26</li><li>27</li><li>28</li><li>29</li><li class="off">30</li><li>31</li></ol>
  </section>
  <section class="month" style="left:627px;top:469px">
    <h2>JUNI</h2>
    <ol class="weekdays"><li>MO</li><li>DI</li><li>MI</li><li>DO</li><li>FR</li><li>SA</li><li>SO</li></ol>
    <ol class="days"><li class="s6 off">1</li><li class="off">2</li><li>3</li><li>4</li><li>5</li><li>6</li><li>7</li><li class="off">8</li><li class="off">9</li><li class="off">10</li><li>11</li><li>12</li><li>13</li><li>14</li><li class="off">15</li><li class="off">16</li><li>17</li><li>18</li><li>19</li><li class="off">20</li><li>21</li><li class="off">22</li><li class="off">23</li><li>24</li><li>25</li><li>26</li><li>27</li><li>28</li><li class="off">29</li><li class="off">30</li></ol>
  </section>

  <section class="month" style="left:330px;top:629px">
    <h2>JULI</h2>
    <ol class="weekdays"><li>MO</li><li>DI</li><li>MI</li><li>DO</li><li>FR</li><li>SA</li><li>SO</li></ol>
    <ol class="days"><li>1</li><li>2</li><li>3</li><li>4</li><li>5</li><li class="off">6</li><li class="off">7</li><li>8</li><li>9</li><li>10</li><li>11</li><li>12</li><li class="off">13</li><li class="off">14</li><li>15</li><li>16</li><li>17</li><li>18</li><li>19</li><li class="off">20</li><li class="off">21</li><li>22</li><li>23</li><li>24</li><li>25</li><li>26</li><li class="off">27</li><li class="off">28</li><li>29</li><li>30</li><li>31</li></ol>
  </section>
  <section class="month" style="left:479px;top:629px">
    <h2>AUGUST</h2>
    <ol class="weekdays"><li>MO</li><li>DI</li><li>MI</li><li>DO</li><li>FR</li><li>SA</li><li>SO</li></ol>
    <ol class="days"><li class="s4">1</li><li>2</li><li class="off">3</li><li class="off">4</li><li>5</li><li>6</li><li>7</li><li>8</li><li>9</li><li class="off">10</li><li class="off">11</li><li>12</li><li>13</li><li>14</li><li>15</li><li>16</li><li class="off">17</li><li class="off">18</li><li>19</li><li>20</li><li>21</li><li>22</li><li>23</li><li class="off">24</li><li class="off">25</li><li>26</li><li>27</li><li>28</li><li>29</li><li>30</li><li class="off">31</li></ol>
  </section>
  <section class="month six" style="left:627px;top:629px">
    <h2>SEPTEMBER</h2>
    <ol class="weekdays"><li>MO</li><li>DI</li><li>MI</li><li>DO</li><li>FR</li><li>SA</li><li>SO</li></ol>
    <ol class="days"><li class="s7 off">1</li><li>2</li><li>3</li><li>4</li><li>5</li><li>6</li><li class="off">7</li><li class="off">8</li><li>9</li><li>10</li><li>11</li><li>12</li><li>13</li><li class="off">14</li><li class="off">15</li><li>16</li><li>17</li><li>18</li><li>19</li><li>20</li><li class="off">21</li><li class="off">22</li><li>23</li><li>24</li><li>25</li><li>26</li><li>27</li><li class="off">28</li><li class="off">29</li><li>30</li></ol>
  </section>

  <section class="month" style="left:330px;top:792px">
    <h2>OKTOBER</h2>
    <ol class="weekdays"><li>MO</li><li>DI</li><li>MI</li><li>DO</li><li>FR</li><li>SA</li><li>SO</li></ol>
    <ol class="days"><li class="s2">1</li><li>2</li><li class="off">3</li><li>4</li><li class="off">5</li><li class="off">6</li><li>7</li><li>8</li><li>9</li><li>10</li><li>11</li><li class="off">12</li><li class="off">13</li><li>14</li><li>15</li><li>16</li><li>17</li><li>18</li><li class="off">19</li><li class="off">20</li><li>21</li><li>22</li><li>23</li><li>24</li><li>25</li><li class="off">26</li><li class="off">27</li><li>28</li><li>29</li><li>30</li><li>31</li></ol>
  </section>
  <section class="month" style="left:479px;top:792px">
    <h2>NOVEMBER</h2>
    <ol class="weekdays"><li>MO</li><li>DI</li><li>MI</li><li>DO</li><li>FR</li><li>SA</li><li>SO</li></ol>
    <ol class="days"><li class="s5">1</li><li class="off">2</li><li class="off">3</li><li>4</li><li>5</li><li>6</li><li>7</li><li>8</li><li class="off">9</li><li class="off">10</li><li>11</li><li>12</li><li>13</li><li>14</li><li>15</li><li class="off">16</li><li class="off">17</li><li>18</li><li>19</li><li>20</li><li>21</li><li>22</li><li class="off">23</li><li class="off">24</li><li>25</li><li>26</li><li>27</li><li>28</li><li>29</li><li class="off">30</li></ol>
  </section>
  <section class="month six" style="left:627px;top:792px">
    <h2>DEZEMBER</h2>
    <ol class="weekdays"><li>MO</li><li>DI</li><li>MI</li><li>DO</li><li>FR</li><li>SA</li><li>SO</li></ol>
    <ol class="days"><li class="s7 off">1</li><li>2</li><li>3</li><li>4</li><li>5</li><li>6</li><li class="off">7</li><li class="off">8</li><li>9</li><li>10</li><li>11</li><li>12</li><li>13</li><li class="off">14</li><li class="off">15</li><li>16</li><li>17</li><li>18</li><li>19</li><li>20</li><li class="off">21</li><li class="off">22</li><li>23</li><li>24</li><li class="off">25</li><li class="off">26</li><li>27</li><li class="off">28</li><li class="off">29</li><li>30</li><li>31</li></ol>
  </section>

  <!-- Folgejahr -->
  <section class="month next" style="left:330px;top:956px">
    <h2>JANUAR</h2>
    <ol class="weekdays"><li>MO</li><li>DI</li><li>MI</li><li>DO</li><li>FR</li><li>SA</li><li>SO</li></ol>
    <ol class="days"><li class="s3 off">1</li><li>2</li><li>3</li><li class="off">4</li><li class="off">5</li><li>6</li><li>7</li><li>8</li><li>9</li><li>10</li><li class="off">11</li><li class="off">12</li><li>13</li><li>14</li><li>15</li><li>16</li><li>17</li><li class="off">18</li><li class="off">19</li><li>20</li><li>21</li><li>22</li><li>23</li><li>24</li><li class="off">25</li><li class="off">26</li><li>27</li><li>28</li><li>29</li><li>30</li><li>31</li></ol>
  </section>
  <section class="month next" style="left:479px;top:956px">
    <h2>FEBRUAR</h2>
    <ol class="weekdays"><li>MO</li><li>DI</li><li>MI</li><li>DO</li><li>FR</li><li>SA</li><li>SO</li></ol>
    <ol class="days"><li class="s6 off">1</li><li class="off">2</li><li>3</li><li>4</li><li>5</li><li>6</li><li>7</li><li class="off">8</li><li class="off">9</li><li>10</li><li>11</li><li>12</li><li>13</li><li>14</li><li class="off">15</li><li class="off">16</li><li>17</li><li>18</li><li>19</li><li>20</li><li>21</li><li class="off">22</li><li class="off">23</li><li>24</li><li>25</li><li>26</li><li>27</li><li>28</li><li class="off">29</li></ol>
  </section>
</div>
</body>
</html>
```